Awesome photographers card for an awesome new business

Double sided business card Black background and silver logo in middle on one side. Details on otherside. please keep it simple

Industry/Entity Type

Photographer

Contact Information for Business Card

Colin Fairweather
0452816307
ColinFairweatherPhotography57@mailvane.com
www.ColinFairweatherPhotography.com.au
Instagram _Colin_fairweather

Requirements
Must have
• My logo in Silver
• please use instagram logo instead of "Instagram"

```html
<!DOCTYPE html>
<html lang="en">
<head>
<meta charset="utf-8">
<title>Colin Fairweather Photography – Business Card</title>
<link rel="stylesheet" href="https://fonts.googleapis.com/css2?family=Lato:wght@300;400;700&display=swap">
<style>
  :root {
    --backdrop: #2b2b2b;
    --card: #0b0b0b;
    --silver: #e6e6e6;
    --silver-soft: #cfcfcf;
  }
  * { margin: 0; padding: 0; box-sizing: border-box; }
  html, body { width: 1200px; height: 880px; overflow: hidden; }
  body {
    background: var(--backdrop);
    font-family: "Lato", Arial, sans-serif;
    position: relative;
  }
  .card {
    position: absolute;
    width: 520px;
    height: 300px;
    background: var(--card);
    overflow: hidden;
    box-shadow: 0 10px 30px rgba(0,0,0,0.5);
  }
  .card--front { left: 90px; top: 130px; }
  .card--back { left: 590px; top: 440px; }

  .brand {
    position: absolute;
    left: 50%; top: 50%;
    transform: translate(-50%, -50%);
    display: flex;
    align-items: center;
    gap: 14px;
    white-space: nowrap;
  }
  .brand__dot {
    width: 22px; height: 22px;
    border-radius: 50%;
    background: var(--silver);
    flex: none;
  }
  .brand__name {
    color: var(--silver);
    font-weight: 400;
    font-size: 24px;
    letter-spacing: 2px;
    text-transform: uppercase;
  }

  .backdrop-name {
    position: absolute;
    left: -18px; top: 18px;
    color: var(--silver);
    font-weight: 300;
    font-size: 120px;
    line-height: 1;
    letter-spacing: -2px;
    white-space: nowrap;
  }

  .details {
    position: absolute;
    left: 232px; top: 128px;
    color: var(--silver);
  }
  .details__name {
    font-weight: 700;
    font-size: 17px;
    letter-spacing: 0.5px;
    text-transform: uppercase;
    margin-bottom: 14px;
  }
  .contact-list { list-style: none; }
  .contact-list li {
    display: flex;
    align-items: center;
    gap: 7px;
    font-size: 12.5px;
    line-height: 19px;
    color: var(--silver-soft);
  }
  .contact-icon {
    width: 13px; height: 13px;
    flex: none;
  }
  .details__web {
    margin-top: 16px;
    font-size: 12.5px;
    color: var(--silver-soft);
  }
</style>
</head>
<body>

  <section class="card card--front" aria-label="Card front">
    <div class="brand">
      <span class="brand__dot"></span>
      <span class="brand__name">Colin Fairweather</span>
    </div>
  </section>

  <section class="card card--back" aria-label="Card back">
    <div class="backdrop-name" aria-hidden="true">Colin</div>

    <div class="details">
      <h1 class="details__name">Colin Fairweather</h1>
      <ul class="contact-list">
        <li>
          <svg class="contact-icon" viewBox="0 0 14 14" aria-label="Phone">
            <circle cx="7" cy="7" r="6.3" fill="none" stroke="#cfcfcf" stroke-width="1"/>
            <path d="M4.6 4 L5.8 3.8 L6.3 5.4 L5.5 6 Q6.2 7.6 7.9 8.4 L8.5 7.6 L10.1 8.1 L9.9 9.4 Q6.6 9.8 4.6 4 Z" fill="#cfcfcf"/>
          </svg>
          0452816307
        </li>
        <li>
          <svg class="contact-icon" viewBox="0 0 14 14" aria-label="Email">
            <circle cx="7" cy="7" r="6.3" fill="none" stroke="#cfcfcf" stroke-width="1"/>
            <rect x="3.8" y="4.8" width="6.4" height="4.4" fill="none" stroke="#cfcfcf" stroke-width="0.9"/>
            <path d="M3.8 4.8 L7 7.3 L10.2 4.8" fill="none" stroke="#cfcfcf" stroke-width="0.9"/>
          </svg>
          ColinFairweatherPhotography57@mailvane.com
        </li>
        <li>
          <svg class="contact-icon" viewBox="0 0 14 14" aria-label="Social profile">
            <circle cx="7" cy="7" r="6.3" fill="none" stroke="#cfcfcf" stroke-width="1"/>
          </svg>
          _Colin_fairweather
        </li>
      </ul>
      <p class="details__web">www.ColinFairweatherPhotography.com.au</p>
    </div>
  </section>

</body>
</html>
```